Website design for an award-winning animation studio

We are an animation studio launching our new corporate website. We need a web designer/developer to produce a professional business website for us. We have competitors' websites and a early web demo/web layout for reference. We cater to the global audience.

Attached is the brief to website designer. There are 4 points of brief details for the designer. Please read through. We will provide the images only after award.

Target Market(s)

Our website caters to potential B2B clients, investors, fellow media & animation industry players, future employees, parents, kids, whoever wants to know us better.

Industry/Entity Type

Business

Number of Pages Required

5+ page

Requirements
Must have
• Brief 1: Reference sites
• For the key reference site: https://yaywow.pelmorcast.com/insider/2016/04/22/quiet-gears-debut/. The color and font gives a very current day feel.
• Other references:
• Demo site: http://vantrel-studios.com/temp/web_beta.html
• Current site: http://vantrel-studios.com/
• Some more References sites:
• http://www.korblint.com/
• https://thepelmorcastcompany.com/
• http://www.quillbarrowanimation.com/
• Brief 2: Template
• Template to use:
• http://themes.kitplankfolio.com/lumina-v1.2.0/sample-04-half-image-slider.html
• Brief 3: Images
• Images to use: We will pass you the images once upon award
• Brief 4: Cater to content
• I attached the word doc. This is a brief for the website designer to get a sense of what content the website will cater to.
• Our website caters to potential B2B clients, investors, fellow industry players, future employees, parents, kids, whoever wants to know us better.
• Our content write up will be professional yet fun, positive and engaging.

```html
<!DOCTYPE html>
<html lang="en">
<head>
<meta charset="utf-8">
<title>Vantrel Studios</title>
<link href="https://fonts.googleapis.com/css2?family=Nunito+Sans:ital,wght@0,400;0,600;0,700;0,800;1,400;1,700&display=swap" rel="stylesheet">
<style>
:root{
  --red:#e8213a;
  --maroon:#9a0f2b;
  --footer:#8f0b28;
  --cyan:#2fe3ea;
  --yellow:#e6ea3a;
  --blue:#1784b9;
  --icon:#2b78a8;
  --icon-ring:#1c4f78;
  --team-ring:#22b9bf;
  --ink:#1c1c1c;
  --muted:#555;
  --line:#c9c9c9;
  --white:#fff;
}
*{box-sizing:border-box;margin:0;padding:0}
html,body{width:1200px;height:5248px;overflow:hidden}
body{position:relative;background:var(--white);font-family:"Nunito Sans",Arial,sans-serif;color:var(--ink)}
.abs{position:absolute}
.ph{position:absolute;display:block}

/* nav */
.topbar{left:0;top:0;width:1200px;height:63px;background:var(--red);z-index:3}
.brand{left:84px;top:17px;display:flex;align-items:center;gap:10px;color:var(--white);font-weight:800;font-size:20px;letter-spacing:1px}
.brand i{width:22px;height:22px;border-radius:50%;background:var(--white);display:block}
.nav{right:86px;top:22px;display:flex;gap:24px;list-style:none}
.nav li{color:var(--white);font-weight:800;font-size:14px;letter-spacing:.3px}

/* hero */
.hero{left:0;top:0;width:1200px;height:490px;
  background:
    radial-gradient(ellipse 250px 60px at 590px 330px,#f0a540 0%,#e08a2e 60%,rgba(224,138,46,0) 100%),
    radial-gradient(ellipse 70px 95px at 440px 260px,#f3c89a 0%,#d79b6a 55%,rgba(215,155,106,0) 100%),
    radial-gradient(ellipse 70px 95px at 560px 250px,#f6d2a8 0%,#4a8fd0 60%,rgba(74,143,208,0) 100%),
    radial-gradient(ellipse 70px 95px at 680px 250px,#e9b789 0%,#5bb04a 60%,rgba(91,176,74,0) 100%),
    radial-gradient(ellipse 85px 110px at 800px 280px,#e2a552 0%,#c57f2e 60%,rgba(197,127,46,0) 100%),
    radial-gradient(ellipse 70px 160px at 1015px 210px,#e24b3c 0%,#c9802f 55%,rgba(201,128,47,0) 100%),
    radial-gradient(ellipse 60px 120px at 345px 250px,#5a4a3c 0%,#8e7a62 55%,rgba(142,122,98,0) 100%),
    radial-gradient(ellipse 60px 70px at 335px 50px,#7c8fe0 0%,rgba(124,143,224,0) 100%),
    linear-gradient(180deg,#b9c3ef 0%,#d2d8f6 55%,#dfe2f4 80%,#eeecf2 100%)}
.hero-line{left:0;top:143px;width:1200px;text-align:center;color:var(--white);font-weight:700;font-style:italic;font-size:30px;text-shadow:0 1px 3px rgba(60,70,140,.35)}
.dots{left:578px;top:452px;display:flex;gap:8px}
.dots b{width:9px;height:9px;border-radius:50%;background:rgba(255,255,255,.6)}
.dots b:first-child{background:var(--white)}

/* showcase */
.showcase-label{top:505px;font-weight:800;font-size:17px;letter-spacing:.5px}
.frame{top:528px;height:242px;border:10px solid;display:flex;gap:10px;padding:8px}
.frame .ph{position:static;flex:1;height:100%}
.f-shorts{left:80px;width:516px;border-color:var(--cyan)}
.f-tv{left:616px;width:354px;border-color:var(--yellow)}
.f-games{left:990px;width:130px;border-color:var(--red);flex-direction:column}

/* headings */
.tag{height:49px;background:var(--maroon);color:var(--white);font-weight:800;font-size:30px;line-height:49px;padding-left:14px;border-left:6px solid var(--white);box-shadow:-6px 0 0 var(--maroon)}
.body-text{font-size:18px;line-height:1.75;color:var(--ink)}

/* story */
.story-text{left:98px;top:940px;width:545px}
.story-text p+p{margin-top:20px}
.team-pic{width:140px;height:140px;border-radius:50%;border:8px solid var(--team-ring)}

/* band */
.grass{left:0;top:1320px;width:1200px;height:238px;
  background:
    radial-gradient(ellipse 300px 60px at 200px 200px,rgba(190,190,90,.55),rgba(190,190,90,0)),
    radial-gradient(ellipse 300px 60px at 950px 210px,rgba(200,190,90,.5),rgba(200,190,90,0)),
    repeating-linear-gradient(95deg,rgba(30,40,15,.25) 0 3px,rgba(0,0,0,0) 3px 11px),
    linear-gradient(180deg,#2f3a24 0%,#4e6128 40%,#7a8c36 72%,#aaa652 100%)}
.band-brand{left:0;top:1398px;width:1200px;display:flex;justify-content:center;align-items:center;gap:12px;color:#8fd33a;font-weight:800;font-size:40px;letter-spacing:2px}
.band-brand i{width:30px;height:30px;border-radius:50%;background:#2a2a3a;display:block}
.band-line{left:0;top:1504px;width:1200px;text-align:center;color:var(--white);font-weight:700;font-size:16px}

/* work */
.filters{left:84px;top:1757px;display:flex;gap:12px}
.filters span{height:32px;padding:0 12px;border:2px solid var(--cyan);color:var(--blue);font-weight:800;font-size:13px;line-height:28px;background:#e9fdfe}
.filters span.on{background:var(--blue);color:var(--white);border-color:var(--blue)}
.tile{width:326px;height:182px}

/* services */
.svc{width:180px;text-align:center}
.svc-icon{width:119px;height:119px;margin:0 auto;border-radius:50%;background:var(--icon);border:6px solid var(--icon-ring);display:flex;align-items:center;justify-content:center}
.svc-name{margin-top:14px;color:var(--icon-ring);font-weight:800;font-size:22px;line-height:1.15}

/* partners */
.partners{left:0;top:3115px;width:1200px;height:427px;background:var(--blue)}
.partners-line{left:84px;top:3190px;color:var(--white);font-size:19px;font-weight:600}
.badge{top:3270px;height:80px;background:rgba(255,255,255,.35)}

/* careers */
.careers-text{left:84px;top:3822px;width:1040px;font-size:19px;line-height:1.8}
.careers-text p+p{margin-top:18px}
.hunt{left:84px;top:4036px;font-weight:800;font-size:22px}
.roles{left:120px;top:4110px;font-style:italic;font-size:18px;line-height:56px}

/* contact */
.contact-rule{left:0;top:4366px;width:1200px;height:2px;background:var(--line)}
.enquire{left:78px;top:4450px;width:520px;font-size:19px;line-height:1.4}
.enquire a{color:var(--blue);text-decoration:none}
.loc-title{left:84px;top:4576px;font-weight:700;font-size:21px}
.loc{font-size:12px;line-height:1.45;font-weight:600}
.field{left:648px;width:465px;border-bottom:2px solid var(--line);font-size:16px;color:var(--muted);padding-bottom:10px}
.send{left:658px;top:4858px;width:88px;height:40px;background:var(--cyan);color:var(--white);font-weight:800;font-size:13px;text-align:center;line-height:40px}

/* footer */
.footer{left:0;top:4963px;width:1200px;height:252px;background:var(--footer)}
.legal{left:0;top:5215px;width:1200px;height:33px;background:var(--red);color:var(--white);font-size:12px;font-weight:700;line-height:33px;padding-left:84px}
</style>
</head>
<body>

<div class="abs hero ph" role="img" aria-label="Illustration of cartoon kids and a bear at a classroom table with numbers"></div>
<p class="abs hero-line">We believe in creating for kids and kids-at-heart</p>
<div class="abs dots"><b></b><b></b><b></b></div>

<header class="abs topbar">
  <div class="abs brand"><i></i>VANTREL</div>
  <ul class="abs nav">
    <li>OUR STORY</li><li>WORK</li><li>SERVICES</li><li>PARTNERS</li><li>NEWS</li><li>CAREERS</li><li>CONTACT</li>
  </ul>
</header>

<span class="abs showcase-label" style="left:84px;color:var(--cyan)">SHORTS</span>
<span class="abs showcase-label" style="left:616px;color:#c4c820">TV SERIES</span>
<span class="abs showcase-label" style="left:990px;color:var(--red)">GAMES</span>
<div class="abs frame f-shorts">
  <span class="ph" role="img" aria-label="Short film poster with a gnome character" style="background:radial-gradient(ellipse 60% 35% at 50% 18%,#e8d9a4,rgba(232,217,164,0)),radial-gradient(ellipse 45% 35% at 50% 65%,#b5452f,rgba(181,69,47,0)),linear-gradient(170deg,#8b6a2c,#3f4a1f)"></span>
  <span class="ph" role="img" aria-label="Short film poster with a desert landscape" style="background:radial-gradient(ellipse 40% 30% at 50% 60%,#4a4740,rgba(74,71,64,0)),linear-gradient(180deg,#e0ddd4 0%,#b9b3a5 45%,#6b665a 100%)"></span>
  <span class="ph" role="img" aria-label="Short film poster with a ship on the sea" style="background:radial-gradient(ellipse 45% 28% at 50% 52%,#6d4b2c,rgba(109,75,44,0)),linear-gradient(180deg,#9cc0da 0%,#5f8fb3 50%,#2c3e4c 100%)"></span>
</div>
<div class="abs frame f-tv">
  <span class="ph" role="img" aria-label="TV series poster with a lion character" style="background:radial-gradient(ellipse 45% 35% at 50% 55%,#e2a24a,rgba(226,162,74,0)),radial-gradient(ellipse 50% 12% at 50% 12%,#f4e36a,rgba(244,227,106,0)),linear-gradient(180deg,#8cc94a,#3d7a2a)"></span>
  <span class="ph" role="img" aria-label="TV series poster with a counting cartoon girl" style="background:radial-gradient(ellipse 40% 30% at 50% 62%,#f2c9a0,rgba(242,201,160,0)),radial-gradient(ellipse 50% 14% at 50% 14%,#7ccf4e,rgba(124,207,78,0)),linear-gradient(180deg,#f2c14a,#5ea3d6)"></span>
</div>
<div class="abs frame f-games">
  <span class="ph" role="img" aria-label="Game icon with a cartoon character" style="background:radial-gradient(circle at 50% 60%,#f3c9a0 0 25%,rgba(243,201,160,0) 50%),linear-gradient(180deg,#6ab3ea,#2f7ec1)"></span>
  <span class="ph" role="img" aria-label="Game icon with a cartoon character" style="background:radial-gradient(circle at 50% 55%,#6fb94a 0 25%,rgba(111,185,74,0) 50%),linear-gradient(180deg,#f0a93a,#d9562f)"></span>
</div>

<h2 class="abs tag" style="left:84px;top:847px;width:224px">Our Story</h2>
<h2 class="abs tag" style="left:815px;top:847px;width:298px">Team</h2>
<div class="abs story-text body-text">
  <p>Vantrel Studios is an award-winning animation and interactive studio based in Singapore, with offices in California, USA and Bangalore, India.</p>
  <p>We create original characters and stories for kids and grown-ups (who are really just plus-sized kids), and we fuse the creative with the latest in interactive technology to bring our content to wherever our fans are.</p>
</div>
<span class="abs team-pic" role="img" aria-label="Team member portrait photo" style="left:812px;top:931px;background:radial-gradient(ellipse 35% 42% at 50% 48%,#c9a184,rgba(201,161,132,0) 100%),radial-gradient(ellipse 60% 40% at 50% 100%,#2e3440,rgba(46,52,64,0)),linear-gradient(180deg,#9aa0a6,#5c6068)"></span>
<span class="abs team-pic" role="img" aria-label="Team member portrait photo" style="left:980px;top:931px;background:radial-gradient(ellipse 35% 42% at 50% 48%,#d2ab8a,rgba(210,171,138,0) 100%),radial-gradient(ellipse 60% 40% at 50% 100%,#4a4a4a,rgba(74,74,74,0)),linear-gradient(180deg,#c9c4bb,#7b776f)"></span>
<span class="abs team-pic" role="img" aria-label="Team member portrait photo" style="left:812px;top:1102px;background:radial-gradient(ellipse 35% 42% at 50% 48%,#cfa78b,rgba(207,167,139,0) 100%),radial-gradient(ellipse 60% 40% at 50% 100%,#222,rgba(34,34,34,0)),linear-gradient(180deg,#b8bcc2,#6a6e74)"></span>
<span class="abs team-pic" role="img" aria-label="Team member portrait photo" style="left:980px;top:1102px;background:radial-gradient(ellipse 35% 42% at 50% 48%,#b98c6c,rgba(185,140,108,0) 100%),radial-gradient(ellipse 60% 40% at 50% 100%,#1e1e1e,rgba(30,30,30,0)),linear-gradient(180deg,#a9a39a,#57534d)"></span>

<div class="abs grass ph" role="img" aria-label="Close-up photograph of a grass field"></div>
<div class="abs band-brand"><i></i>VANTREL</div>
<p class="abs band-line">We Believe in Melding Creativity with Technology</p>

<h2 class="abs tag" style="left:84px;top:1677px;width:212px">Our Work</h2>
<div class="abs filters"><span class="on">ALL</span><span>TV</span><span>GAME</span><span>FILM</span><span>COMMERCIAL</span><span>AR/VR</span></div>
<span class="abs tile ph" role="img" aria-label="Cartoon kids with numbers in a classroom" style="left:84px;top:1813px;background:radial-gradient(ellipse 35% 25% at 55% 70%,#eea043,rgba(238,160,67,0)),radial-gradient(ellipse 12% 30% at 30% 55%,#f0c79c,rgba(240,199,156,0)),radial-gradient(ellipse 12% 30% at 72% 55%,#4a8fd0,rgba(74,143,208,0)),radial-gradient(ellipse 30% 20% at 25% 12%,#f6c64a,rgba(246,198,74,0)),linear-gradient(180deg,#c5d3f3,#e6e0ee)"></span>
<span class="abs tile ph" style="left:438px;top:1813px;background:radial-gradient(ellipse 40% 40% at 50% 50%,#666,#4f4f4f)" role="img" aria-label="Project thumbnail with hover overlay"></span>
<svg class="abs" style="left:576px;top:1879px" width="50" height="50" viewBox="0 0 50 50"><circle cx="21" cy="21" r="13" fill="none" stroke="#fff" stroke-width="4"/><line x1="31" y1="31" x2="44" y2="44" stroke="#fff" stroke-width="5" stroke-linecap="round"/></svg>
<span class="abs tile ph" role="img" aria-label="Cartoon girl next to a tablet app" style="left:791px;top:1813px;background:radial-gradient(ellipse 25% 35% at 75% 45%,#5fb9e6,rgba(95,185,230,0)),radial-gradient(ellipse 16% 35% at 28% 62%,#f0c79c,rgba(240,199,156,0)),radial-gradient(ellipse 20% 18% at 28% 30%,#5a3a28,rgba(90,58,40,0)),linear-gradient(135deg,#b9dcf2,#e9c99a)"></span>
<span class="abs tile ph" role="img" aria-label="Animated ship scene" style="left:84px;top:2023px;background:radial-gradient(ellipse 30% 40% at 70% 55%,#8a6a3e,rgba(138,106,62,0)),radial-gradient(ellipse 22% 30% at 25% 60%,#5e4a35,rgba(94,74,53,0)),linear-gradient(180deg,#9ebad1 0%,#7a9fbf 45%,#4d5a63 100%)"></span>
<span class="abs tile ph" role="img" aria-label="Gnome short film still" style="left:438px;top:2023px;background:radial-gradient(ellipse 35% 20% at 50% 35%,#e9d8a0,rgba(233,216,160,0)),radial-gradient(ellipse 15% 30% at 60% 75%,#b5452f,rgba(181,69,47,0)),linear-gradient(180deg,#9a7a32,#3f4a1f)"></span>
<span class="abs tile ph" role="img" aria-label="Robot in a desert film still" style="left:791px;top:2023px;background:radial-gradient(ellipse 22% 45% at 50% 55%,#4c5044,rgba(76,80,68,0)),linear-gradient(180deg,#d8d4c8 0%,#b8b3a3 50%,#6e6b5f 100%)"></span>
<span class="abs tile ph" role="img" aria-label="Dark interior animated scene" style="left:84px;top:2236px;background:radial-gradient(ellipse 25% 30% at 40% 40%,#a0708a,rgba(160,112,138,0)),radial-gradient(ellipse 20% 25% at 80% 70%,#6d5a70,rgba(109,90,112,0)),linear-gradient(135deg,#4b3a4a,#2a2a33)"></span>
<span class="abs tile ph" role="img" aria-label="Cartoon kids in a colourful scene" style="left:438px;top:2236px;background:radial-gradient(ellipse 12% 30% at 30% 60%,#e94b6a,rgba(233,75,106,0)),radial-gradient(ellipse 12% 30% at 55% 60%,#f2c14a,rgba(242,193,74,0)),radial-gradient(ellipse 12% 30% at 78% 60%,#5bb04a,rgba(91,176,74,0)),linear-gradient(135deg,#9b7be0,#6fcde8)"></span>
<span class="abs tile ph" role="img" aria-label="Building model with a screen" style="left:791px;top:2236px;background:radial-gradient(ellipse 18% 35% at 62% 50%,#6a5442,rgba(106,84,66,0)),radial-gradient(ellipse 12% 14% at 30% 30%,#7fc6ea,rgba(127,198,234,0)),linear-gradient(135deg,#e2d5c2,#7a6856)"></span>

<h2 class="abs tag" style="left:84px;top:2541px;width:170px">Services</h2>
<p class="abs body-text" style="left:98px;top:2640px;font-size:19px">Vantrel Studios produce or co-produce animeted series and films for distribution internationally</p>
<div class="abs svc" style="left:60px;top:2750px"><div class="svc-icon"><svg width="46" height="30" viewBox="0 0 46 30"><polyline points="12,5 3,15 12,25" fill="none" stroke="#fff" stroke-width="3.5"/><polyline points="34,5 43,15 34,25" fill="none" stroke="#fff" stroke-width="3.5"/><line x1="26" y1="3" x2="20" y2="27" stroke="#fff" stroke-width="3.5"/></svg></div><div class="svc-name">TV</div></div>
<div class="abs svc" style="left:239px;top:2750px"><div class="svc-icon"><svg width="46" height="30" viewBox="0 0 46 30"><polyline points="12,5 3,15 12,25" fill="none" stroke="#fff" stroke-width="3.5"/><polyline points="34,5 43,15 34,25" fill="none" stroke="#fff" stroke-width="3.5"/><line x1="26" y1="3" x2="20" y2="27" stroke="#fff" stroke-width="3.5"/></svg></div><div class="svc-name">COMERCIAL</div></div>
<div class="abs svc" style="left:418px;top:2750px"><div class="svc-icon"><svg width="46" height="30" viewBox="0 0 46 30"><polyline points="12,5 3,15 12,25" fill="none" stroke="#fff" stroke-width="3.5"/><polyline points="34,5 43,15 34,25" fill="none" stroke="#fff" stroke-width="3.5"/><line x1="26" y1="3" x2="20" y2="27" stroke="#fff" stroke-width="3.5"/></svg></div><div class="svc-name">FILM</div></div>
<div class="abs svc" style="left:596px;top:2750px"><div class="svc-icon"><svg width="46" height="30" viewBox="0 0 46 30"><polyline points="12,5 3,15 12,25" fill="none" stroke="#fff" stroke-width="3.5"/><polyline points="34,5 43,15 34,25" fill="none" stroke="#fff" stroke-width="3.5"/><line x1="26" y1="3" x2="20" y2="27" stroke="#fff" stroke-width="3.5"/></svg></div><div class="svc-name">CO<br>PRODUCTION</div></div>
<div class="abs svc" style="left:775px;top:2750px"><div class="svc-icon"><svg width="46" height="30" viewBox="0 0 46 30"><polyline points="12,5 3,15 12,25" fill="none" stroke="#fff" stroke-width="3.5"/><polyline points="34,5 43,15 34,25" fill="none" stroke="#fff" stroke-width="3.5"/><line x1="26" y1="3" x2="20" y2="27" stroke="#fff" stroke-width="3.5"/></svg></div><div class="svc-name">MOTION<br>CAPTURE</div></div>
<div class="abs svc" style="left:953px;top:2750px"><div class="svc-icon"><svg width="46" height="30" viewBox="0 0 46 30"><polyline points="12,5 3,15 12,25" fill="none" stroke="#fff" stroke-width="3.5"/><polyline points="34,5 43,15 34,25" fill="none" stroke="#fff" stroke-width="3.5"/><line x1="26" y1="3" x2="20" y2="27" stroke="#fff" stroke-width="3.5"/></svg></div><div class="svc-name">AR/VE</div></div>

<div class="abs partners"></div>
<h2 class="abs tag" style="left:84px;top:3070px;width:220px">Partners</h2>
<p class="abs partners-line">No man is an island, and our partners have been instrumental in our journey</p>
<span class="abs badge" style="left:84px;width:60px;border-radius:4px"></span>
<span class="abs badge" style="left:186px;width:150px;border-radius:4px"></span>
<span class="abs badge" style="left:376px;width:150px;height:40px;top:3290px;border-radius:4px"></span>
<span class="abs badge" style="left:548px;width:150px;border-radius:4px"></span>
<span class="abs badge" style="left:718px;width:150px;border-radius:4px"></span>
<span class="abs badge" style="left:904px;width:70px;border-radius:50%"></span>
<span class="abs badge" style="left:1010px;width:100px;border-radius:4px"></span>

<h2 class="abs tag" style="left:84px;top:3665px;width:220px">Careers</h2>
<div class="abs careers-text">
  <p>We're a team of professionals. We have the animator, the director, the producer, the writer, the artist, the technologist, the gamer, the coder, the business guy, the office mama.</p>
  <p>Keeping everyone on deck is a shared belief in respect for teamwork, open communication and collaboration, with a bias for action and an intolerance for BS.</p>
</div>
<p class="abs hunt">Currently, we're on the hunt for:</p>
<ul class="abs roles"><li>Assistant Producer</li><li>Assistant Director</li></ul>

<div class="abs contact-rule"></div>
<h2 class="abs tag" style="left:84px;top:4368px;width:222px">Contact Us</h2>
<p class="abs enquire">For projects, co-production and general enquiries: <a>hello@vantrel-studios.com</a></p>
<p class="abs loc-title">Our locations</p>
<p class="abs loc" style="left:84px;top:4622px">Singapore (Main Office)<br>12 Harlow Lane<br>#03-08 Fennick Building<br>Singapore 100001</p>
<p class="abs loc" style="left:330px;top:4622px">United States<br>48 Corvel Street<br>Suite 210<br>Pinecrest, CA 90001</p>
<p class="abs loc" style="left:84px;top:4752px">Bangalore<br>Unit 4B, Level 5<br>Orrin Block<br>Tech Park<br>Bangalore 560001</p>
<div class="abs field" style="top:4500px">Name</div>
<div class="abs field" style="top:4572px">Email Address</div>
<div class="abs field" style="top:4652px;height:194px">Message</div>
<div class="abs send">SEND</div>

<div class="abs footer"></div>
<div class="abs legal">Copyright © 2016 · Vantrel Studios. All Rights Reserved</div>

</body>
</html>
```